Lead Sales Portal Needs to Generate B2B Signup's

We are looking for banner ad designs to drive new business (B2B) traffic to our insurance and mortgage industry self serve lead sites. The sites are HomeLoanProspectHub.com and PolicyBuyerHub.com, and we service over 45,000 insurance agents and mortgage lenders in a self serve lead portal model. We want our banners to generate more of these clients.

Our clients come to our sites, browse our database and then pick out and purchase the consumer leads that they need to generate new business.

We advertise extensively on Zyntrix and on other PPC platforms, and our existing banners are looking really tired.

Some of the ad copy that works well for us is:

Cherry Pick Your Life Leads - Why Pay More Than $3.50 For Life Insurance Leads?
Sign up today and we'll match up to $250

Agents - Here's $250 For New Clients. Cherry Pick Your Life Insurance Leads & Save! Sign up today and we'll match up to $250

One of our Landing Pages that performs well is here:
http://www.policybuyerhub.com/lp/008/

One of our competitors ad's are here:

http://www.brellow.com/search/results?q=QuoteMarten&ad=427360

We're looking for a design that is eye catching, uses our "Deeply Discounted Leads" and our "$250 match bonus"

This is the second contest that we have for the same sites. The previous designs were great and really performed well, so we are looking for new designs now that 6 months have passed. I have uploaded some winning banners from the last group for your information.

Reason: I've been asked by some of the designers to delay a day to get their designs in. I'm happy to do it!

Target Market(s)

These are insurance agents and mortgage lenders. All of our clients are business' or individuals within the business. This is a B2B campaign, so we need something that is professional and upscale. These are NOT consumer facing ad's!

Industry/Entity Type

Insurance

Font styles to use
Sans Serif

Requirements
Must have
• We must have the logos for the sites in the banners. Also, we must have a call to action arrow and "Go" button. Some animation is necessary, (especially around the arrow and the GO button).

One or two designs.

File type

.JPEG
.JPG
.PNG
.GIF

File size

150 KB or smaller

Image sizes

Vertical rectangle: 240 x 400
Mobile leaderboard: 320 x 50
Banner: 468 x 60
Leaderboard: 728 x 90
Square: 250 x 250
Small square: 200 x 200
Large rectangle: 336 x 280
Inline rectangle: 300 x 250
Skyscraper: 120 x 600
Wide skyscraper: 160 x 600
Half-page: 300 x 600
Large leaderboard: 970 x 90

```html
<!DOCTYPE html>
<html lang="en">
<head>
<meta charset="utf-8">
<title>Policy Buyer Hub – Banner Set</title>
<link rel="stylesheet" href="https://fonts.googleapis.com/css2?family=Bebas+Neue&family=Ubuntu:wght@400;500;700&display=swap">
<style>
  :root {
    --board: #3a2415;
    --logo-top: #ffffff;
    --logo-bottom: #d9d9d9;
    --ink: #1d1d1d;
    --sky-top: #cfe0f2;
    --sky-mid: #a9c8ea;
    --sky-low: #7ea9dc;
    --bubble: #ffffff;
    --cta-top: #2f2f2f;
    --cta-bottom: #040404;
    --cta-text: #ffffff;
    --go-top: #ffe772;
    --go-bottom: #f3b400;
    --go-ink: #1a1a1a;
  }
  * { box-sizing: border-box; margin: 0; padding: 0; }
  html, body { width: 1200px; height: 607px; overflow: hidden; }
  body { background: var(--board); position: relative; font-family: "Ubuntu", sans-serif; color: var(--ink); }

  .slot { position: absolute; transform: scale(0.902); transform-origin: 0 0; box-shadow: 0 4px 10px rgba(0,0,0,.55); }
  .ad { display: flex; overflow: hidden; background: #fff; }
  .ad--row { flex-direction: row; }
  .ad--col { flex-direction: column; }

  /* logo panel */
  .brand { display: flex; align-items: center; justify-content: center; gap: 8px;
           background: linear-gradient(var(--logo-top), var(--logo-bottom)); flex: none; }
  .brand--stack { flex-direction: column; gap: 4px; }
  .brand-mark { border-radius: 50%; background: var(--ink); flex: none; }
  .brand-name { font-family: "Ubuntu", sans-serif; font-weight: 400; color: var(--ink); white-space: nowrap; }

  /* photo scene */
  .scene { position: relative; flex: none; overflow: hidden; }
  .scene-photo { position: absolute; inset: 0;
                 background: linear-gradient(160deg, var(--sky-top) 0%, var(--sky-mid) 50%, var(--sky-low) 100%); }
  .scene-bubble { position: absolute; inset: 0; }
  .bubble-text { position: absolute; text-align: center; font-weight: 500; color: var(--ink); }
  .bubble-text strong { font-weight: 700; }

  /* call to action */
  .cta { flex: none; display: flex; flex-direction: column; align-items: center; justify-content: center;
         background: linear-gradient(var(--cta-top), var(--cta-bottom)); color: var(--cta-text); }
  .cta-text { font-family: "Bebas Neue", sans-serif; text-align: center; text-shadow: 0 0 6px rgba(255,255,255,.35); }
  .cta-amount { display: block; }
  .cta-action { display: flex; align-items: center; }
  .cta-arrow { fill: none; stroke: var(--cta-text); stroke-linecap: round; stroke-linejoin: round; }
  .go { display: inline-flex; align-items: center; justify-content: center; gap: 3px;
        background: linear-gradient(var(--go-top), var(--go-bottom)); color: var(--go-ink);
        font-family: "Ubuntu", sans-serif; font-weight: 700; border-radius: 999px; }
  .go-tip { width: 0; height: 0; border-style: solid; border-color: transparent transparent transparent var(--go-ink); }

  /* large leaderboard 970x90 */
  .ad--970 { width: 970px; height: 90px; }
  .ad--970 .brand { width: 205px; }
  .ad--970 .brand-mark { width: 36px; height: 36px; }
  .ad--970 .brand-name { font-size: 19px; }
  .ad--970 .scene { width: 562px; }
  .ad--970 .bubble-text { left: 60px; width: 270px; top: 5px; font-size: 22px; line-height: 26px; }
  .ad--970 .cta { width: 203px; gap: 4px; }
  .ad--970 .cta-text { font-size: 25px; line-height: 24px; }
  .ad--970 .cta-arrow { width: 90px; height: 18px; stroke-width: 2.5; }
  .ad--970 .cta-action { gap: 12px; }
  .ad--970 .go { width: 58px; height: 24px; font-size: 15px; }
  .ad--970 .go-tip { border-width: 6px 0 6px 8px; }

  /* leaderboard 728x90 */
  .ad--728 { width: 728px; height: 90px; }
  .ad--728 .brand { width: 108px; }
  .ad--728 .brand-mark { width: 22px; height: 22px; }
  .ad--728 .brand-name { font-size: 10.5px; }
  .ad--728 .scene { width: 417px; }
  .ad--728 .bubble-text { left: 0; width: 270px; top: 5px; font-size: 22px; line-height: 26px; }
  .ad--728 .cta { width: 203px; gap: 4px; }
  .ad--728 .cta-text { font-size: 25px; line-height: 24px; }
  .ad--728 .cta-arrow { width: 90px; height: 18px; stroke-width: 2.5; }
  .ad--728 .cta-action { gap: 12px; }
  .ad--728 .go { width: 58px; height: 24px; font-size: 15px; }
  .ad--728 .go-tip { border-width: 6px 0 6px 8px; }

  /* banner 468x60 */
  .ad--468 { width: 468px; height: 60px; }
  .ad--468 .brand { width: 70px; }
  .ad--468 .brand-mark { width: 18px; height: 18px; }
  .ad--468 .brand-name { font-size: 7.5px; }
  .ad--468 .scene { width: 267px; }
  .ad--468 .bubble-text { left: 1px; width: 170px; top: 4px; font-size: 14px; line-height: 17px; }
  .ad--468 .cta { width: 131px; gap: 2px; }
  .ad--468 .cta-text { font-size: 14.5px; line-height: 15px; }
  .ad--468 .cta-arrow { width: 54px; height: 12px; stroke-width: 2; }
  .ad--468 .cta-action { gap: 8px; }
  .ad--468 .go { width: 36px; height: 15px; font-size: 9.5px; }
  .ad--468 .go-tip { border-width: 4px 0 4px 5px; }

  /* mobile leaderboard 320x50 */
  .ad--320 { width: 320px; height: 50px; }
  .ad--320 .brand { width: 70px; }
  .ad--320 .brand-mark { width: 16px; height: 16px; }
  .ad--320 .brand-name { font-size: 7.5px; }
  .ad--320 .scene { width: 133px; }
  .ad--320 .bubble-text { left: 0; width: 133px; top: 4px; font-size: 11px; line-height: 14px; }
  .ad--320 .cta { width: 117px; gap: 2px; }
  .ad--320 .cta-text { font-size: 12.5px; line-height: 12.5px; }
  .ad--320 .cta-arrow { width: 44px; height: 10px; stroke-width: 2; }
  .ad--320 .cta-action { gap: 6px; }
  .ad--320 .go { width: 32px; height: 13px; font-size: 8.5px; }
  .ad--320 .go-tip { border-width: 3.5px 0 3.5px 4.5px; }

  /* skyscrapers 120x600 / 160x600 */
  .ad--120 { width: 120px; height: 600px; }
  .ad--160 { width: 160px; height: 600px; }
  .ad--col .brand { height: 95px; width: 100%; }
  .ad--col .scene { height: 307px; width: 100%; }
  .ad--col .cta { height: 198px; width: 100%; gap: 6px; }
  .ad--120 .brand-mark { width: 36px; height: 36px; }
  .ad--120 .brand-name { font-size: 12.5px; }
  .ad--120 .bubble-text { left: 0; width: 120px; top: 22px; font-size: 16.5px; line-height: 21px; }
  .ad--120 .bubble-text strong { font-size: 25px; line-height: 30px; display: block; }
  .ad--120 .cta-text { font-size: 25px; line-height: 35px; }
  .ad--120 .cta-amount { font-size: 46px; line-height: 48px; }
  .ad--120 .cta-arrow { width: 50px; height: 14px; stroke-width: 2; }
  .ad--120 .cta-action { gap: 6px; }
  .ad--120 .go { width: 56px; height: 22px; font-size: 14px; }
  .ad--120 .go-tip { border-width: 5px 0 5px 7px; }
  .ad--160 .brand-mark { width: 40px; height: 40px; }
  .ad--160 .brand-name { font-size: 16.5px; }
  .ad--160 .bubble-text { left: 0; width: 160px; top: 14px; font-size: 20.5px; line-height: 26px; }
  .ad--160 .bubble-text strong { font-size: 29px; line-height: 34px; display: block; }
  .ad--160 .cta-text { font-size: 32px; line-height: 34px; }
  .ad--160 .cta-amount { font-size: 58px; line-height: 60px; }
  .ad--160 .cta-arrow { width: 64px; height: 16px; stroke-width: 2.2; }
  .ad--160 .cta-action { gap: 8px; }
  .ad--160 .go { width: 58px; height: 22px; font-size: 14px; }
  .ad--160 .go-tip { border-width: 5px 0 5px 7px; }
</style>
</head>
<body>

<!-- skyscraper 120x600 -->
<div class="slot" style="left:17px; top:25px;">
  <div class="ad ad--col ad--120">
    <div class="brand brand--stack"><span class="brand-mark"></span><span class="brand-name">Policy Buyer Hub</span></div>
    <div class="scene">
      <div class="scene-photo" role="img" aria-label="Smiling businessman in shirt and red tie working at a laptop among clouds"></div>
      <svg class="scene-bubble" viewBox="0 0 120 307" aria-hidden="true">
        <ellipse cx="60" cy="72" rx="76" ry="84" fill="#fff"/>
        <polygon points="35,140 28,212 70,150" fill="#fff"/>
      </svg>
      <p class="bubble-text"><strong>AGENTS!</strong>Why pay more than $3.50 for life insurance leads?</p>
    </div>
    <div class="cta">
      <p class="cta-text">Sign up today<br>and we will<br>match up to<span class="cta-amount">$250!</span></p>
      <div class="cta-action">
        <svg class="cta-arrow" viewBox="0 0 60 14"><path d="M2 9 Q28 4 54 8"/><path d="M48 4 L55 8 L48 12"/></svg>
        <span class="go">GO<span class="go-tip"></span></span>
      </div>
    </div>
  </div>
</div>

<!-- wide skyscraper 160x600 -->
<div class="slot" style="left:143px; top:25px;">
  <div class="ad ad--col ad--160">
    <div class="brand brand--stack"><span class="brand-mark"></span><span class="brand-name">Policy Buyer Hub</span></div>
    <div class="scene">
      <div class="scene-photo" role="img" aria-label="Smiling businessman in shirt and red tie working at a laptop among clouds"></div>
      <svg class="scene-bubble" viewBox="0 0 160 307" aria-hidden="true">
        <ellipse cx="80" cy="72" rx="96" ry="86" fill="#fff"/>
        <polygon points="45,145 38,215 90,152" fill="#fff"/>
      </svg>
      <p class="bubble-text"><strong>AGENTS!</strong>Why pay more than $3.50 for life insurance leads?</p>
    </div>
    <div class="cta">
      <p class="cta-text">Sign up today<br>and we will<br>match up to<span class="cta-amount">$250!</span></p>
      <div class="cta-action">
        <svg class="cta-arrow" viewBox="0 0 60 14"><path d="M2 9 Q28 4 54 8"/><path d="M48 4 L55 8 L48 12"/></svg>
        <span class="go">GO<span class="go-tip"></span></span>
      </div>
    </div>
  </div>
</div>

<!-- large leaderboard 970x90 -->
<div class="slot" style="left:308px; top:25px;">
  <div class="ad ad--row ad--970">
    <div class="brand"><span class="brand-mark"></span><span class="brand-name">Policy Buyer Hub</span></div>
    <div class="scene">
      <div class="scene-photo" role="img" aria-label="Smiling businessman in shirt and red tie working at a laptop among clouds"></div>
      <svg class="scene-bubble" viewBox="0 0 562 90" aria-hidden="true">
        <ellipse cx="195" cy="46" rx="136" ry="44" fill="#fff"/>
        <polygon points="300,22 410,30 312,48" fill="#fff"/>
      </svg>
      <p class="bubble-text"><strong>AGENTS!</strong> Why pay<br>more than $3.50 for<br>life insurance leads?</p>
    </div>
    <div class="cta">
      <p class="cta-text">Sign up today and we<br>will match up to $250!</p>
      <div class="cta-action">
        <svg class="cta-arrow" viewBox="0 0 90 18"><path d="M2 13 Q45 4 84 10"/><path d="M77 5 L85 10 L77 15"/></svg>
        <span class="go">GO<span class="go-tip"></span></span>
      </div>
    </div>
  </div>
</div>

<!-- leaderboard 728x90 -->
<div class="slot" style="left:313px; top:120px;">
  <div class="ad ad--row ad--728">
    <div class="brand brand--stack"><span class="brand-mark"></span><span class="brand-name">Policy Buyer Hub</span></div>
    <div class="scene">
      <div class="scene-photo" role="img" aria-label="Smiling businessman in shirt and red tie working at a laptop among clouds"></div>
      <svg class="scene-bubble" viewBox="0 0 417 90" aria-hidden="true">
        <ellipse cx="135" cy="46" rx="128" ry="44" fill="#fff"/>
        <polygon points="232,22 345,30 244,48" fill="#fff"/>
      </svg>
      <p class="bubble-text"><strong>AGENTS!</strong> Why pay<br>more than $3.50 for<br>life insurance leads?</p>
    </div>
    <div class="cta">
      <p class="cta-text">Sign up today and we<br>will match up to $250!</p>
      <div class="cta-action">
        <svg class="cta-arrow" viewBox="0 0 90 18"><path d="M2 13 Q45 4 84 10"/><path d="M77 5 L85 10 L77 15"/></svg>
        <span class="go">GO<span class="go-tip"></span></span>
      </div>
    </div>
  </div>
</div>

<!-- banner 468x60 -->
<div class="slot" style="left:313px; top:214px;">
  <div class="ad ad--row ad--468">
    <div class="brand brand--stack"><span class="brand-mark"></span><span class="brand-name">Policy Buyer Hub</span></div>
    <div class="scene">
      <div class="scene-photo" role="img" aria-label="Smiling businessman in shirt and red tie working at a laptop among clouds"></div>
      <svg class="scene-bubble" viewBox="0 0 267 60" aria-hidden="true">
        <ellipse cx="86" cy="31" rx="86" ry="30" fill="#fff"/>
        <polygon points="150,16 218,22 156,33" fill="#fff"/>
      </svg>
      <p class="bubble-text"><strong>AGENTS!</strong> Why pay<br>more than $3.50 for<br>life insurance leads?</p>
    </div>
    <div class="cta">
      <p class="cta-text">Sign up today and we<br>will match up to $250!</p>
      <div class="cta-action">
        <svg class="cta-arrow" viewBox="0 0 54 12"><path d="M2 9 Q26 3 49 7"/><path d="M44 3 L50 7 L44 10"/></svg>
        <span class="go">GO<span class="go-tip"></span></span>
      </div>
    </div>
  </div>
</div>

<!-- mobile leaderboard 320x50 -->
<div class="slot" style="left:313px; top:282px;">
  <div class="ad ad--row ad--320">
    <div class="brand brand--stack"><span class="brand-mark"></span><span class="brand-name">Policy Buyer Hub</span></div>
    <div class="scene">
      <div class="scene-photo" role="img" aria-label="Smiling businessman in shirt and red tie working at a laptop among clouds"></div>
      <svg class="scene-bubble" viewBox="0 0 133 50" aria-hidden="true">
        <ellipse cx="66" cy="25" rx="70" ry="25" fill="#fff"/>
      </svg>
      <p class="bubble-text"><strong>AGENTS!</strong> Why pay<br>more than $3.50 for<br>life insurance leads?</p>
    </div>
    <div class="cta">
      <p class="cta-text">Sign up today and we<br>will match up to $250!</p>
      <div class="cta-action">
        <svg class="cta-arrow" viewBox="0 0 44 10"><path d="M2 7 Q21 2 40 6"/><path d="M36 2.5 L41 6 L36 9"/></svg>
        <span class="go">GO<span class="go-tip"></span></span>
      </div>
    </div>
  </div>
</div>

</body>
</html>
```